Online Trading Web-Design

Web design is required for a new startup that specialises in online trading between buyers and sellers of fashion apparel. The company is called: Bright Cove Hub (bch)

Website needs to be clean and css friendly. we like the idea of having a largish "banner" on the homepage which we can rotate using HTML5. examples of the banners are: http://au.plevrix.com/ ; http://www.dorvanqe.com.au/

the logo has been established already, please limit designs around the colors already established (see uploaded logo).
Updates

Hi, a few clarifications:

1. although the website deals in online trading for clothes etc. the main focus of the website needs to be about highlighting trading between buyers (clothing stores) and sellers (clothing brands). so the website wont be directly selling items of clothes etc.

Industry/Entity Type

Fashion

```html
<!DOCTYPE html>
<html lang="en">
<head>
<meta charset="utf-8">
<title>Bright Cove Hub</title>
<link href="https://fonts.googleapis.com/css2?family=Source+Sans+3:wght@300;400;600;700&display=swap" rel="stylesheet">
<style>
:root{
  --cyan:#00dbe8;
  --cyan-dark:#00bccb;
  --brand:#4fc4d0;
  --teal-text:#2fd3e0;
  --ink:#444;
  --muted:#777;
  --line:#d8d8d8;
  --band:#efefef;
  --white:#fff;
}
*{box-sizing:border-box;margin:0;padding:0}
html,body{width:1200px;height:1200px;overflow:hidden;background:var(--white);font-family:"Source Sans 3",sans-serif;color:var(--ink)}
.page{position:relative;width:1200px;height:1200px}
.abs{position:absolute}
.top-rule{left:0;top:0;width:1200px;height:9px;background:#bdbdbd}

.brand{left:134px;top:70px;font-size:42px;font-weight:600;line-height:1;color:var(--brand);white-space:nowrap}

.social{display:flex;gap:9px}
.social span{width:22px;height:22px;border-radius:3px;display:block}
.s1{background:#3b5998}.s2{background:#4fc3f0}.s3{background:#f48a1e}.s4{background:#f57d00}.s5{background:#1c6fa6}
.social-top{left:897px;top:68px}

.search{left:835px;top:113px;width:220px;height:36px;border:1px solid var(--line);border-radius:5px;box-shadow:0 3px 4px rgba(0,0,0,.08);font-size:11px;color:#555;padding:10px 16px}
.search svg{position:absolute;right:12px;top:8px}

.nav{left:0;top:190px;width:1200px;height:57px;background:linear-gradient(#2ef0f8,var(--cyan) 50%,var(--cyan-dark));border-bottom:3px solid #9feaf0}
.nav ul{list-style:none;display:flex;justify-content:center;gap:44px;padding-top:17px}
.nav li{font-size:19px;color:var(--white)}

.hero{left:113px;top:257px;width:970px;height:383px;border-radius:5px;overflow:hidden;border:1px solid #ccc;background:linear-gradient(90deg,#d9d3cb,#cfc8bd 50%,#b9b4ad)}
.hero-shadow{left:140px;top:638px;width:920px;height:28px;background:radial-gradient(ellipse at top,rgba(0,0,0,.22),transparent 70%)}
.hero-photo{position:absolute;left:450px;top:0;width:520px;height:383px;background:linear-gradient(90deg,rgba(0,0,0,0),rgba(40,60,140,.35) 30%,rgba(70,80,110,.35) 80%,rgba(0,0,0,0))}
.hero-copy{position:absolute;left:0;top:78px;width:440px;text-align:center;color:var(--teal-text);text-shadow:0 2px 3px rgba(0,0,0,.25)}
.hero-copy .h1{font-size:60px;font-weight:600;line-height:1.1;padding-left:30px}
.hero-copy .h2{font-size:35px;font-weight:600;margin-top:6px}
.hero-copy .h3{font-size:104px;font-weight:600;line-height:1}
.dots{display:flex;gap:10px}
.dots span{width:14px;height:14px;border-radius:50%;background:radial-gradient(circle at 40% 35%,#8ff4fa,var(--cyan) 60%,#00a9b8)}
.hero-dots{position:absolute;right:16px;top:13px}

.col-title{font-size:27px;font-weight:300;color:var(--ink);top:676px}
.tile{width:288px;height:155px;top:719px;border-radius:3px}
.tile-1{left:121px;background:linear-gradient(90deg,#5f8c78,#8fb4a0 40%,#6e4b44 55%,#8bb3a2)}
.tile-2{left:447px;background:linear-gradient(90deg,#9a9a9a,#3b3433 40%,#1e1a1a 60%,#c8c8c8)}
.body-copy{width:290px;top:882px;font-size:13px;line-height:22px;color:var(--muted)}
.btn{top:958px;width:105px;height:36px;border-radius:3px;background:linear-gradient(#3ef1f8,var(--cyan-dark));box-shadow:0 2px 3px rgba(0,0,0,.25);color:#134;font-size:14px;text-align:center;line-height:36px}

.brands{left:766px;top:724px;width:300px;display:grid;grid-template-columns:repeat(3,100px);grid-template-rows:50px 50px 50px 76px;align-items:center;justify-items:center}
.brands span{font-size:12px;font-weight:600;color:#555;letter-spacing:.5px}
.brand-dots{left:881px;top:965px}

.newsletter{left:0;top:1017px;width:1200px;height:68px;background:linear-gradient(#f7f7f7,var(--band))}
.nl-title{left:305px;top:1034px;font-size:26px;font-weight:300;color:#555}
.nl-input{left:474px;top:1033px;width:279px;height:36px;border:1px solid #ddd;border-radius:18px;background:var(--white);font-size:14px;color:#888;padding:8px 0 0 44px}
.nl-input svg{position:absolute;left:13px;top:10px}
.nl-btn{left:776px;top:1034px;width:147px;height:36px;border-radius:3px;background:linear-gradient(#34eff7,var(--cyan-dark));box-shadow:0 3px 4px rgba(0,0,0,.2);color:var(--white);font-size:18px;font-weight:700;text-align:center;line-height:36px}

.foot-links{left:124px;top:1104px;font-size:15px;color:var(--ink);display:flex;gap:10px}
.foot-links i{font-style:normal;color:#888}
.copyright{left:123px;top:1139px;font-size:12.5px;color:var(--muted)}
.social-foot{left:907px;top:1108px}
</style>
</head>
<body>
<div class="page">
  <div class="abs top-rule"></div>

  <div class="abs brand">Bright Cove Hub</div>

  <div class="abs social social-top"><span class="s1"></span><span class="s2"></span><span class="s3"></span><span class="s4"></span><span class="s5"></span></div>

  <div class="abs search">Search
    <svg width="18" height="18" viewBox="0 0 18 18"><circle cx="7" cy="7" r="5.5" fill="none" stroke="#777" stroke-width="1.6"/><line x1="11" y1="11" x2="16" y2="16" stroke="#777" stroke-width="2.2" stroke-linecap="round"/></svg>
  </div>

  <nav class="abs nav">
    <ul><li>Home</li><li>About Us</li><li>Latest Clothes</li><li>Best Brands</li><li>News</li><li>Offers</li><li>Testimonials</li></ul>
  </nav>

  <div class="abs hero-shadow"></div>
  <section class="abs hero">
    <div class="hero-photo" role="img" aria-label="Four young people in hoodies and jeans leaning against a concrete wall"></div>
    <div class="hero-copy">
      <div class="h1">New Styles</div>
      <div class="h2">Save upto</div>
      <div class="h3">40%</div>
    </div>
    <div class="dots hero-dots"><span></span><span></span><span></span></div>
  </section>

  <h2 class="abs col-title" style="left:121px">Latest Clothes</h2>
  <div class="abs tile tile-1" role="img" aria-label="Young man in a burgundy blazer and knit vest against a green backdrop"></div>
  <p class="abs body-copy" style="left:123px">Duis tincidunt lectus quis dui viverra vestibulum. Suspendisse vulputate aliquam dui. Nulla elemen-tum dui ut augue. Aliquam vehicula</p>
  <div class="abs btn" style="left:123px">LEARN MORE</div>

  <h2 class="abs col-title" style="left:447px">Top Sellers</h2>
  <div class="abs tile tile-2" role="img" aria-label="Woman in sunglasses, black coat and scarf on a city street"></div>
  <p class="abs body-copy" style="left:449px">Duis tincidunt lectus quis dui viverra vestibulum. Suspendisse vulputate aliquam dui. Nulla elemen-tum dui ut augue. Aliquam vehicula</p>
  <div class="abs btn" style="left:445px">LEARN MORE</div>

  <h2 class="abs col-title" style="left:766px">Our Clothing Brands</h2>
  <div class="abs brands">
    <span>Northfield</span><span>Lumen</span><span>Harbor Row</span>
    <span>Arden</span><span>Velmora</span><span>Tessel Lane</span>
    <span>Kestrel</span><span>Ravelle</span><span>Corvin Denim</span>
    <span>Quill</span><span>Alden Mode</span><span>Pella</span>
  </div>
  <div class="abs dots brand-dots"><span></span><span></span><span></span></div>

  <div class="abs newsletter"></div>
  <div class="abs nl-title">NEWSLETTER</div>
  <div class="abs nl-input">
    <svg width="24" height="16" viewBox="0 0 24 16"><rect x="0.5" y="0.5" width="23" height="15" fill="#888"/><polyline points="1,1 12,9 23,1" fill="none" stroke="#fff" stroke-width="1.6"/><line x1="1" y1="15" x2="9" y2="7" stroke="#fff" stroke-width="1.2"/><line x1="23" y1="15" x2="15" y2="7" stroke="#fff" stroke-width="1.2"/></svg>
    Subscribe your news letter
  </div>
  <div class="abs nl-btn">SUBSCRIBE</div>

  <div class="abs foot-links"><span>Home</span><i>|</i><span>About Us</span><i>|</i><span>Latest Clothes</span><i>|</i><span>Best Brands</span><i>|</i><span>News</span><i>|</i><span>Offers</span><i>|</i><span>Testimonials</span><i>|</i><span>Contact</span></div>
  <div class="abs copyright">© 2013 Company Name.&nbsp; All right reserved.&nbsp; Term of Use</div>
  <div class="abs social social-foot"><span class="s1"></span><span class="s2"></span><span class="s3"></span><span class="s4"></span><span class="s5"></span></div>
</div>
</body>
</html>
```